Webdesign for Brightwell for use on webpage

We aim to deliver insights for power consumers in the nordic market in the B2B market, without being a supplier.

Since we are helping customers in the green transition and reducing CO2 emissions, green colors would be preferred, but we are keeping an open mind. We would like to communicate transperancy, awareness and enabling economic potential for customers.

We deliver our product on a SaaS platform through visualization in dashboards

Target Market(s)

B2B

Industry/Entity Type

Power Consumption

Number of Pages Required

1 page

Colors
0054AA
0677BA
7BADD7
CADEEF
E8F1F8
0094D4
00A9DD
6FCCEA
C7EBF8
E9F6FB
00AB8E
00BBA5
67D7C9
C6EFE9
E9F9F6
59FF00
82FF00
B8FF75
E3FFCB
F4FFEA

Requirements
Must have
• The general looks and color schemes must be in line with logo called "brightwell.eps" - see attached

```html
<!DOCTYPE html>
<html lang="en">
<head>
<meta charset="utf-8">
<title>Brightwell – Energy Data Insights</title>
<link href="https://fonts.googleapis.com/css2?family=Lato:wght@400;700;900&display=swap" rel="stylesheet">
<style>
:root{
  --green:#7dc242;
  --green-dark:#5fa52c;
  --blue:#1a56a6;
  --blue-deep:#0f4c9c;
  --navy:#0a1434;
  --navy-2:#10245a;
  --ink:#444c5a;
  --white:#ffffff;
  --pale:#eef5fb;
}
*{margin:0;padding:0;box-sizing:border-box}
html,body{width:1200px;height:4090px;overflow:hidden}
body{position:relative;font-family:'Lato',sans-serif;background:var(--white);color:var(--ink)}
.abs{position:absolute}
a{color:inherit;text-decoration:none}

/* header */
.site-header{position:absolute;left:0;top:0;width:1200px;height:70px;background:var(--white);z-index:5}
.brand{position:absolute;left:126px;top:-9px;width:144px;height:144px;border-radius:50%;background:var(--white);display:flex;align-items:center;justify-content:center;z-index:6;box-shadow:0 2px 6px rgba(0,0,0,.08)}
.brand span{font-weight:900;font-size:19px;color:var(--blue);letter-spacing:.5px;margin-top:18px}
.main-nav{position:absolute;top:28px;left:289px;font-size:11px;font-weight:700;color:#222}
.main-nav a{position:absolute;white-space:nowrap}
.social-top{position:absolute;top:21px;left:810px;display:flex;gap:5px}
.social-top i{display:block;width:31px;height:31px;border:2px solid var(--blue);border-radius:50%;position:relative}
.social-top i::after{content:"";position:absolute;left:10px;top:10px;width:7px;height:7px;border-radius:50%;background:var(--green)}
.call{position:absolute;left:986px;top:14px}
.call small{display:block;font-size:12px;color:var(--green)}
.call strong{display:block;font-size:21px;color:var(--blue);font-weight:700;margin-top:2px}

/* hero */
.hero{position:absolute;left:0;top:70px;width:1200px;height:650px;background:linear-gradient(90deg,var(--navy) 0%,#0c1a45 55%,#0b1b4b 100%);overflow:hidden}
.hero h1{position:absolute;left:130px;top:142px;width:540px;color:var(--white);font-size:50px;line-height:75px;font-weight:700;letter-spacing:-.5px;white-space:nowrap;z-index:2}
.hero p{position:absolute;left:132px;top:302px;width:460px;color:var(--white);font-size:13px;line-height:32px}
.btn-outline{position:absolute;left:130px;top:385px;width:176px;height:50px;border:2px solid var(--white);border-radius:25px;color:var(--white);font-size:15px;font-weight:700;display:flex;align-items:center;justify-content:center}
.hero-visual{position:absolute;left:694px;top:13px;width:406px;height:406px;border-radius:50%;border:5px solid var(--white);background:radial-gradient(circle at 50% 45%,#2fbf5a 0%,#0c5a3a 35%,#061c2e 75%)}
.hero-glow{position:absolute;left:680px;top:430px;width:460px;height:120px;border-radius:50%;background:radial-gradient(ellipse,#3d7fd6 0%,rgba(30,80,170,.4) 45%,rgba(10,20,52,0) 75%)}
.dots{position:absolute;left:574px;top:532px;display:flex;gap:4px}
.dots i{width:7px;height:7px;border-radius:50%;background:var(--white)}
.dots i:first-child{background:var(--green)}
.wave{position:absolute;left:0;width:1200px}

/* shared headings */
.section-title{position:absolute;font-size:33px;font-weight:900;color:var(--blue);letter-spacing:-.3px;white-space:nowrap}
.section-title em{font-style:normal;color:var(--green)}
.centered{left:0;width:1200px;text-align:center}
.rule{position:absolute;left:580px;width:40px;height:3px;background:var(--green)}

/* about */
.about-visual{position:absolute;left:87px;top:770px;width:498px;height:498px;border-radius:50%;border:7px solid var(--blue-deep);padding:24px}
.about-visual div{width:100%;height:100%;border-radius:50%;background:radial-gradient(circle at 50% 40%,#cfe6c3 0%,#5f9a5a 40%,#e8f1f8 72%,#ffffff 100%)}
.about-text{position:absolute;left:646px;top:860px;width:470px;font-size:13px;line-height:28px}
.btn-blue{position:absolute;height:50px;border-radius:25px;background:var(--blue-deep);color:var(--white);font-size:16px;font-weight:700;display:flex;align-items:center;padding-left:58px}
.btn-blue::before{content:"";position:absolute;left:5px;top:5px;width:40px;height:40px;border-radius:50%;background:var(--white)}

/* services */
.services{position:absolute;left:0;top:1300px;width:1200px;height:800px;background:linear-gradient(180deg,#2a6ab4 0%,#1d5aa8 50%,#2f73c0 100%)}
.arrow-btn{position:absolute;width:36px;height:36px;border-radius:50%;display:flex;align-items:center;justify-content:center}
.card{position:absolute;top:1616px;width:294px;height:281px;background:var(--white);border-radius:4px;text-align:center;padding:0 22px}
.card .icon{width:80px;height:76px;margin:20px auto 0}
.card h3{font-size:15px;font-weight:700;color:var(--blue);margin-top:26px}
.card p{font-size:13px;line-height:24px;margin-top:8px}
.card.featured{background:var(--green);color:var(--white)}
.card.featured h3{color:var(--white)}

/* why */
.why-label{position:absolute;font-size:16px;font-weight:700;color:var(--blue);white-space:nowrap;line-height:20px}
.why-label.right{text-align:right}
.node{position:absolute;width:68px;height:68px;border-radius:50%;background:var(--green);border:3px solid var(--white);box-shadow:0 0 0 2px var(--green)}
.node::after{content:"";position:absolute;left:18px;top:18px;width:26px;height:26px;border:3px solid var(--white);border-radius:50%}

/* blog */
.blog{position:absolute;left:0;top:2857px;width:1200px;height:800px;background:var(--pale)}
.blog-photo{position:absolute}
.post-title{position:absolute;font-size:15px;font-weight:900;color:#222;line-height:28px}
.post-text{position:absolute;font-size:13px;line-height:28px}

/* footer */
.footer{position:absolute;left:0;top:3680px;width:1200px;height:410px;background:linear-gradient(180deg,#1c5db0 0%,#1a54a3 100%);color:var(--white)}
.footer h4{position:absolute;top:122px;font-size:15px;font-weight:700}
.footer ul{position:absolute;top:147px;list-style:none;font-size:14px;line-height:28.3px}
.newsletter{position:absolute;left:833px;top:149px;width:246px;height:43px;background:var(--white);border-radius:2px;font-size:11px;color:#888;padding:14px 16px}
.newsletter svg{position:absolute;right:16px;top:13px}
.social-foot{position:absolute;left:838px;top:240px;display:flex;gap:32px}
.social-foot i{display:block;width:13px;height:13px;border:2px solid var(--green);border-radius:50%}
.footer-rule{position:absolute;left:135px;top:326px;width:931px;height:1px;background:rgba(255,255,255,.5)}
.legal{position:absolute;top:340px;font-size:11px}
</style>
</head>
<body>

<header class="site-header">
  <nav class="main-nav">
    <a style="left:0">HOME</a>
    <a style="left:62px">ABOUT US</a>
    <a style="left:149px">WHY CHOOSE US</a>
    <a style="left:274px">SERVICES</a>
    <a style="left:360px">BLOG</a>
    <a style="left:419px">CONTACT US</a>
  </nav>
  <div class="social-top" aria-label="Social links"><i></i><i></i><i></i><i></i></div>
  <div class="call"><small>Call Us Today!</small><strong>123 555 0190</strong></div>
</header>
<div class="brand"><span>BRIGHTWELL</span></div>

<section class="hero">
  <div class="hero-glow" role="img" aria-label="Glowing low-poly hand holding the bulb"></div>
  <div class="hero-visual" role="img" aria-label="Glowing light bulb with a green tree and rising bar chart inside"></div>
  <h1>BRIGHTWELL ENERGY<br>DATA INSIGHTS</h1>
  <p>Lorem ipsum dolor sit amet, consectetur adipiscing elit sed do eiusmod tempor incididunt ut labore et dolore magna aliqua.</p>
  <a class="btn-outline">GET STARTED</a>
  <div class="dots"><i></i><i></i><i></i><i></i><i></i></div>
</section>
<svg class="wave" style="top:560px" width="1200" height="160" viewBox="0 0 1200 160">
  <path d="M0 80 C300 10 600 170 900 100 C1050 62 1150 40 1200 30 L1200 160 L0 160Z" fill="#7dc242"/>
  <path d="M0 112 C300 58 600 212 900 142 C1050 104 1150 82 1200 72 L1200 160 L0 160Z" fill="#ffffff"/>
</svg>

<!-- About -->
<div class="about-visual"><div role="img" aria-label="Light bulb silhouette filled with a solar panel field and a rising bar chart"></div></div>
<h2 class="section-title" style="left:646px;top:784px">ABOUT <em>BRIGHTWELL</em></h2>
<p class="about-text">Sd ut perspiciatis unde omnis iste natus error sit voluptatem accusantium doloremque laudantium, totam rem aperiam, eaque ipsa quae ab illo inventore veritatis et quasi architecto beatae vitae dicta sunt explicabo. Nemo enim ipsam voluptatem quia voluptas sit aspernatur aut odit aut fugit, sed quia consequuntur magni dolores eos qui ratione voluptatem sequi nesciunt. Neque porro quisquam est, qui dolorem ipsum quia dolor sit amet, consectetur, adipisci velit, sed quia non numquam eius modi tempora incidunt ut labore et dolore magnam aliquam quaerat voluptatem. Ut enim ad minima veniam, quis nostrum exercitationem ullam corporis suscipit laboriosam, nisi ut aliquid ex ea commodi consequaturQuis autem vel eum iure reprehenderit qui in ea voluptate velit esse quam nihil molestiae consequatur, vel illum qui dolorem eum fugiat quo voluptas nulla.</p>
<a class="btn-blue" style="left:646px;top:1220px;width:182px">LEARN MORE</a>

<!-- Services -->
<section class="services" role="img" aria-label="Blue-toned photo of hands holding a young plant">
  <svg class="wave" style="top:0" width="1200" height="120" viewBox="0 0 1200 120">
    <path d="M0 0 L1200 0 L1200 50 C1000 20 800 60 600 80 C400 100 200 90 0 110Z" fill="#ffffff"/>
    <path d="M110 0 C140 40 180 80 300 80 C500 80 700 40 900 45 C1050 48 1150 55 1200 60 L1200 48 C1100 30 1000 25 900 30 C700 25 500 70 300 66 C200 64 150 40 110 0Z" fill="#7dc242"/>
  </svg>
  <svg class="wave" style="top:660px" width="1200" height="140" viewBox="0 0 1200 140">
    <path d="M0 40 C300 0 700 90 1200 30 L1200 62 C700 118 300 34 0 78Z" fill="#7dc242"/>
    <path d="M0 78 C300 34 700 118 1200 62 L1200 140 L0 140Z" fill="#ffffff"/>
  </svg>
</section>
<h2 class="section-title centered" style="top:1508px;color:#fff">OUR SERVICES</h2>
<div class="rule" style="top:1557px"></div>
<div class="arrow-btn" style="left:987px;top:1522px;border:2px solid #fff">
  <svg width="10" height="10" viewBox="0 0 10 10"><path d="M7 1 L3 5 L7 9" stroke="#fff" stroke-width="2" fill="none"/></svg></div>
<div class="arrow-btn" style="left:1029px;top:1522px;background:var(--green)">
  <svg width="10" height="10" viewBox="0 0 10 10"><path d="M3 1 L7 5 L3 9" stroke="#fff" stroke-width="2" fill="none"/></svg></div>

<article class="card" style="left:132px">
  <svg class="icon" viewBox="0 0 80 76"><path d="M10 30 L50 30 L62 70 L22 70Z" fill="none" stroke="#1a56a6" stroke-width="3"/><path d="M20 30 L32 70 M30 30 L42 70 M40 30 L52 70 M13 43 L54 43 M17 57 L58 57" stroke="#1a56a6" stroke-width="2"/><circle cx="66" cy="16" r="7" fill="none" stroke="#7dc242" stroke-width="3"/></svg>
  <h3>SOLAR AS A SERVICE</h3>
  <p>Lorem ipsum dolor sit amet, consectetur adipiscing elit, sed do eiusmod tempor incididunt ut labore et dolore magna aliqua. Quis ipsum suspendisse ultrices gravida.</p>
</article>
<article class="card featured" style="left:454px">
  <svg class="icon" viewBox="0 0 80 76"><path d="M10 6 L70 60 M70 6 L10 60" stroke="#fff" stroke-width="5"/><path d="M30 40 L50 40 L54 74 L26 74Z" fill="none" stroke="#fff" stroke-width="3"/><circle cx="40" cy="33" r="5" fill="#fff"/></svg>
  <h3>WIND GENERATORS SYSTEMS</h3>
  <p>Lorem ipsum dolor sit amet, consectetur adipiscing elit, sed do eiusmod tempor incididunt ut labore et dolore magna aliqua. Quis ipsum suspendisse ultrices gravida.</p>
</article>
<article class="card" style="left:774px">
  <svg class="icon" viewBox="0 0 80 76"><rect x="22" y="12" width="44" height="20" rx="6" fill="none" stroke="#1a56a6" stroke-width="3"/><path d="M44 32 L44 62 L54 62 L54 32" fill="none" stroke="#1a56a6" stroke-width="3"/><path d="M40 72 L58 72" stroke="#1a56a6" stroke-width="3"/><path d="M14 14 Q8 22 14 30 M8 10 Q0 22 8 34" fill="none" stroke="#7dc242" stroke-width="3"/></svg>
  <h3>COMMERCIAL SYSTEMS</h3>
  <p>Lorem ipsum dolor sit amet, consectetur adipiscing elit, sed do eiusmod tempor incididunt ut labore et dolore magna aliqua. Quis ipsum suspendisse ultrices gravida.</p>
</article>

<!-- Why choose us -->
<h2 class="section-title centered" style="top:2183px">WHY <em>CHOOSE US</em></h2>
<svg class="abs" style="left:380px;top:2335px" width="440" height="440" viewBox="0 0 440 440">
  <circle cx="220" cy="220" r="212" fill="none" stroke="#1a56a6" stroke-width="8"/>
</svg>
<div class="abs" style="left:470px;top:2400px;width:260px;height:360px;border-radius:50% 50% 40% 40%;background:radial-gradient(ellipse at 50% 45%,#e6f3da 0%,#bfe19f 45%,#ffffff 80%)" role="img" aria-label="Outlined green light bulb with a rising bar chart and blue base"></div>
<div class="node" style="left:556px;top:2299px"></div>
<div class="node" style="left:712px;top:2370px"></div>
<div class="node" style="left:780px;top:2521px"></div>
<div class="node" style="left:712px;top:2677px"></div>
<div class="node" style="left:410px;top:2677px"></div>
<div class="node" style="left:347px;top:2521px"></div>
<div class="node" style="left:402px;top:2370px"></div>
<div class="why-label centered" style="top:2270px">LONG TIME TO USE</div>
<div class="why-label" style="left:797px;top:2394px">USED FOR MANY PURPOSES</div>
<div class="why-label" style="left:863px;top:2544px">LOW INSTALLATION COSTS</div>
<div class="why-label" style="left:797px;top:2698px">ENERGY CAN BE REUSED</div>
<div class="why-label right" style="right:816px;top:2394px">ALAWAYS CLEAN ENERGY</div>
<div class="why-label right" style="right:862px;top:2544px">EASY INSTALLATION</div>
<div class="why-label right" style="right:816px;top:2698px">EXTENDED GUARANTEE</div>

<!-- Blog -->
<section class="blog"></section>
<h2 class="section-title centered" style="top:2940px">OUR <em>LATEST BLOG</em></h2>
<div class="rule" style="top:2987px"></div>
<div class="blog-photo" style="left:127px;top:3025px;width:436px;height:270px;background:linear-gradient(135deg,#0a1f5a 0%,#1f6fd0 55%,#5cb4f0 100%)" role="img" aria-label="Hand touching a SaaS cloud diagram with connected devices"></div>
<h3 class="post-title" style="left:133px;top:3306px;width:430px">LOREM IPSUM DOLOR SIT AMET CONSECTE TUR ADIPISCING ELIT SED DO</h3>
<p class="post-text" style="left:133px;top:3363px;width:430px">Lorem ipsum dolor sit amet, consectetur adipiscing elit, sed do eiusmod tempor incididunt ut labore et dolore magna aliqua. Quis ipsum suspendisse ultrices gravida Risus commodo.</p>
<a class="btn-blue" style="left:133px;top:3457px;width:182px">LEARN MORE</a>

<div class="blog-photo" style="left:582px;top:3025px;width:196px;height:150px;background:linear-gradient(160deg,#cfe7b4 0%,#7aa85a 55%,#4a3a2c 100%)" role="img" aria-label="Hand holding soil with a green seedling"></div>
<h3 class="post-title" style="left:797px;top:3026px;width:290px">LOREM IPSUM DOLOR SIT AMET ISCING ELITSED DO EIUSM</h3>
<p class="post-text" style="left:797px;top:3086px;width:285px">Lorem ipsum dolor sit amet, consectetur adipiscing elit, sed do eiusmod tempor incididunt ut labore et dolore.</p>

<div class="blog-photo" style="left:582px;top:3191px;width:196px;height:150px;background:linear-gradient(160deg,#2a2f36 0%,#5a4a3e 55%,#d98a3a 100%)" role="img" aria-label="Hands at a laptop with a glowing light bulb"></div>
<h3 class="post-title" style="left:797px;top:3192px;width:290px">LOREM IPSUM DOLOR SIT AMET ISCING ELITSED DO EIUSM</h3>
<p class="post-text" style="left:797px;top:3252px;width:285px">Lorem ipsum dolor sit amet, consectetur adipiscing elit, sed do eiusmod tempor incididunt ut labore et dolore.</p>

<div class="blog-photo" style="left:582px;top:3357px;width:196px;height:150px;background:radial-gradient(circle at 50% 45%,#d6f0a0 0%,#5e9a32 45%,#1f3f1a 100%)" role="img" aria-label="Hand holding a glowing globe surrounded by eco icons"></div>
<h3 class="post-title" style="left:797px;top:3358px;width:290px">LOREM IPSUM DOLOR SIT AMET ISCING ELITSED DO EIUSM</h3>
<p class="post-text" style="left:797px;top:3418px;width:285px">Lorem ipsum dolor sit amet, consectetur adipiscing elit, sed do eiusmod tempor incididunt ut labore et dolore.</p>

<!-- Footer -->
<svg class="wave" style="top:3540px" width="1200" height="160" viewBox="0 0 1200 160">
  <path d="M110 10 C130 70 170 110 260 112 C500 118 750 70 1000 80 C1100 84 1160 90 1200 92 L1200 160 L0 160 L0 150 C60 130 90 80 110 10Z" fill="#7dc242"/>
  <path d="M0 152 C200 120 500 150 750 120 C900 102 1100 100 1200 108 L1200 160 L0 160Z" fill="#1c5db0"/>
</svg>
<footer class="footer">
  <div class="abs" style="left:189px;top:106px;width:118px;height:118px;border-radius:50%;border:3px solid #fff"></div>
  <div class="abs" style="left:120px;top:236px;width:256px;text-align:center;font-size:34px;font-weight:900;letter-spacing:.5px">BRIGHTWELL</div>

  <h4 style="left:430px">QUICK LINKS</h4>
  <ul style="left:430px"><li>Home</li><li>About us</li><li>Why Choose Us</li><li>Services</li><li>Blog</li><li>Contact Us</li></ul>

  <h4 style="left:600px">SERVICES</h4>
  <ul style="left:600px"><li>Solar As A Service</li><li>Solar PV Systems</li><li>Wind Generators Systems</li><li>Commercial Systems</li></ul>

  <h4 style="left:832px">SUBSCRIBE THE NEWSLETTERS</h4>
  <div class="newsletter">Enter The Email
    <svg width="16" height="16" viewBox="0 0 16 16"><path d="M1 8 L15 1 L11 15 L8 9Z" fill="#7dc242"/></svg>
  </div>
  <div class="social-foot" aria-label="Social links"><i></i><i></i><i></i><i></i><i></i></div>

  <div class="footer-rule"></div>
  <div class="legal" style="left:135px">© Copyrights 2021 Brightwell &nbsp;|&nbsp; All Rights Reserved</div>
  <div class="legal" style="left:855px">Privacy Policy &nbsp;|&nbsp; Term And Conditions</div>
</footer>

</body>
</html>
```